Electrical business needs a flyer design

we need a Trifold flyer designed for an electrical company. Our service include new installations, renovations and rewires, safety checks, switchboard upgrades, services and breakdown, home automation and power monitoring. we would like to see designs using dark grey, orange and blue. the final designs should communicate a friendly but professional service. I have attached my old business brochure to indicate the service we provide
Target Market(s)
home owners
Industry/Entity Type
Electrical
Look and feel
Each slider illustrates characteristics of the customer's brand and the style your logo design should communicate.

```html
<!DOCTYPE html>
<html lang="en">
<head>
<meta charset="utf-8">
<title>Crestline Electrical – Trifold Brochure</title>
<link href="https://fonts.googleapis.com/css2?family=Montserrat:wght@600;700;800&family=Roboto:wght@400;500&display=swap" rel="stylesheet">
<style>
  :root {
    --orange: #e8742a;
    --orange-deep: #df5f18;
    --blue: #2a9bd6;
    --blue-dark: #1f7fb8;
    --ink: #2b2b2b;
    --body: #3a3a3a;
    --paper: #f7f7f7;
    --paper-shade: #ebebeb;
    --page-bg: #dfe3e6;
  }
  * { box-sizing: border-box; margin: 0; padding: 0; }
  html, body { width: 1200px; height: 900px; overflow: hidden; }
  body { background: var(--page-bg); font-family: "Roboto", Arial, sans-serif; color: var(--body); }

  .brochure {
    position: absolute; left: 30px; top: 47px; width: 1140px; height: 806px;
    background: var(--paper); box-shadow: 0 10px 30px rgba(0,0,0,.15); overflow: hidden;
  }
  .brochure__shapes { position: absolute; inset: 0; }
  .fold { position: absolute; top: 0; bottom: 0; width: 14px; }
  .fold--first { left: 373px; background: linear-gradient(90deg, rgba(0,0,0,0), rgba(0,0,0,.06), rgba(0,0,0,0)); }
  .fold--second { left: 753px; background: linear-gradient(90deg, rgba(0,0,0,0), rgba(0,0,0,.05), rgba(0,0,0,0)); }

  .panel { position: absolute; top: 0; width: 380px; height: 806px; }
  .panel--services { left: 0; }
  .panel--about { left: 380px; }
  .panel--cover { left: 760px; }

  .photo-electrician { position: absolute; left: 0; top: 0; width: 380px; height: 390px; }

  .intro-text { position: absolute; left: 40px; top: 405px; width: 300px; font-size: 11px; line-height: 1.5; }

  .headline { font-family: "Montserrat", Arial, sans-serif; font-weight: 700; color: var(--ink); }
  .headline--accredited { position: absolute; left: 40px; top: 495px; font-size: 22px; line-height: 1.1; }
  .headline--accredited .accent { display: block; color: var(--orange); font-size: 40px; font-weight: 700; letter-spacing: 1px; }

  .benefits { position: absolute; left: 40px; top: 588px; width: 320px; list-style: none; }
  .benefits li { position: relative; padding-left: 44px; font-size: 10px; line-height: 1.4; margin-bottom: 9px; min-height: 30px; }
  .benefits li::before { content: ""; position: absolute; left: 6px; top: 8px; width: 16px; height: 16px; border-radius: 50%; background: var(--blue); }

  .about-title { position: absolute; left: 40px; top: 54px; font-family: "Montserrat", Arial, sans-serif; font-weight: 800; font-size: 42px; color: var(--orange); }
  .about-text { position: absolute; left: 40px; top: 116px; width: 300px; font-size: 11.5px; line-height: 1.5; }
  .about-text p + p { margin-top: 12px; }

  .service-emblem { position: absolute; left: 100px; top: 320px; width: 180px; height: 180px; }

  .contact { position: absolute; left: 40px; top: 560px; width: 320px; }
  .contact__title { font-family: "Montserrat", Arial, sans-serif; font-weight: 700; font-size: 26px; color: var(--ink); }
  .contact__title .accent { color: var(--blue); }
  .contact__rule { width: 60px; height: 3px; background: var(--blue); margin: 8px 0 16px; }
  .contact__list { list-style: none; font-size: 14px; line-height: 1.45; color: var(--ink); }
  .contact__label { font-family: "Montserrat", Arial, sans-serif; font-weight: 600; color: var(--blue); margin-right: 4px; }
  .contact__gap { margin-left: 12px; }
  .contact__address { display: inline-block; vertical-align: top; }

  .brand { position: absolute; left: 60px; top: 50px; display: flex; align-items: center; gap: 12px; }
  .brand__mark { width: 34px; height: 34px; border-radius: 50%; background: var(--blue); }
  .brand__name { font-family: "Montserrat", Arial, sans-serif; font-weight: 700; font-size: 24px; color: var(--blue); }

  .photo-spark { position: absolute; left: 55px; top: 115px; width: 270px; height: 270px; }

  .tagline { position: absolute; left: 56px; top: 455px; font-family: "Montserrat", Arial, sans-serif; font-weight: 800; }
  .tagline__lead { display: block; font-size: 26px; font-weight: 700; color: var(--ink); }
  .tagline__main { display: block; font-size: 52px; line-height: 1; color: var(--orange); }
  .tagline__rule { width: 56px; height: 4px; background: var(--orange); margin-top: 14px; }
</style>
</head>
<body>
  <main class="brochure">
    <svg class="brochure__shapes" width="1140" height="806" viewBox="0 0 1140 806" aria-hidden="true">
      <path d="M0 0 H360 C 420 120 390 310 250 440 C 170 500 80 490 0 470 Z" fill="var(--paper-shade)"/>
      <path d="M380 0 H760 V 420 C 650 330 520 330 380 420 Z" fill="#f2f2f2"/>
      <path d="M760 0 H1140 V 520 C 1040 420 900 440 760 400 Z" fill="#efefef"/>
      <circle cx="950" cy="250" r="152" fill="#e2e2e2"/>
      <path d="M1140 560 C 1070 610 1050 700 990 806 H1140 Z" fill="var(--orange-deep)"/>
    </svg>
    <div class="fold fold--first"></div>
    <div class="fold fold--second"></div>

    <section class="panel panel--services">
      <svg class="photo-electrician" viewBox="0 0 380 390" role="img" aria-label="Photo of an electrician's hands working with a screwdriver on a switchboard">
        <defs>
          <linearGradient id="switchboardTone" x1="0" y1="0" x2="1" y2="1">
            <stop offset="0" stop-color="#c9ccd0"/>
            <stop offset=".55" stop-color="#a9adb2"/>
            <stop offset="1" stop-color="#d8b9a2"/>
          </linearGradient>
        </defs>
        <path d="M0 0 H320 C 380 80 370 260 250 375 H0 Z" fill="url(#switchboardTone)"/>
      </svg>

      <p class="intro-text">We offer a 24-hour, seven-day emergency response service where you need an electrician due to a breakdown or other disruption to your power supply. Our electrical contractors will identify the fault and have your power back on as soon as possible.</p>

      <h2 class="headline headline--accredited">Accredited master<span class="accent">ELECTRICIAN</span></h2>

      <ul class="benefits">
        <li>Electrical work is one of the most dangerous tasks that can be performed in a home or business. Every year, dozens of people are electrocuted or shocked by substandard electrical work.</li>
        <li>By choosing a Master Electrician, you are choosing a contractor whose safety systems are accredited and monitored, and who provides a workmanship guarantee.</li>
        <li>Master Electricians are reliable contractors who provide excellent services and information, potentially saving you time and money.</li>
      </ul>
    </section>

    <section class="panel panel--about">
      <h2 class="about-title">About us</h2>
      <div class="about-text">
        <p>Crestline is a privately owned business providing a comprehensive range of domestic, commercial and industrial electrical services.</p>
        <p>We provide a comprehensive range of electrical and communication services including small jobs around the home to large industrial applications. Our business is underpinned by a commitment to customer service, that is, we turn up on time providing quality workmanship at a fair and competitive price.</p>
      </div>

      <svg class="service-emblem" viewBox="0 0 180 180" role="img" aria-label="Illustration of a fist gripping a lightning bolt inside a circle">
        <circle cx="90" cy="90" r="78" fill="none" stroke="var(--blue)" stroke-width="12"/>
        <circle cx="90" cy="90" r="60" fill="#d6ebf7"/>
      </svg>

      <div class="contact">
        <h3 class="contact__title"><span class="accent">Get in</span> touch now :</h3>
        <div class="contact__rule"></div>
        <ul class="contact__list">
          <li><span class="contact__label">Phone :</span>0400 123 456<span class="contact__gap"></span><span class="contact__label">Fax :</span>8600 1234</li>
          <li><span class="contact__label">E-mail :</span>hello@crestlineelectrical.com</li>
          <li><span class="contact__label">Address :</span><span class="contact__address">PO Box 1480 Riverton<br>SA 5400</span></li>
        </ul>
      </div>
    </section>

    <section class="panel panel--cover">
      <div class="brand">
        <span class="brand__mark"></span>
        <span class="brand__name">Crestline Electrical</span>
      </div>

      <svg class="photo-spark" viewBox="0 0 270 270" role="img" aria-label="Glowing orange lightning bolt on a dark background">
        <defs>
          <radialGradient id="sparkTone" cx=".55" cy=".45" r=".6">
            <stop offset="0" stop-color="#e06a22"/>
            <stop offset=".45" stop-color="#8a3410"/>
            <stop offset="1" stop-color="#3a1608"/>
          </radialGradient>
        </defs>
        <circle cx="135" cy="135" r="135" fill="url(#sparkTone)"/>
      </svg>

      <h1 class="tagline">
        <span class="tagline__lead">For all your</span>
        <span class="tagline__main">Electrical</span>
        <span class="tagline__main">needs</span>
        <div class="tagline__rule"></div>
      </h1>
    </section>
  </main>
</body>
</html>
```